Southport Billboard for Hiring more CDL drivers

I need a catch design for a bill board (size 10ft by 36 ft) to catch the attention for semi truck drivers.
In the design I want it to include:
-My company logo along with my website(brisklanefreighters.com) and my number(503-217-6095) for contact info.
-I also need it to say earn up to $90,000 a year
-I will send a few photos to choose from
-I need the logo to look clean and simple! I don't want it to be cluttered just clean, simple and catchy.!

Target Market(s)

CDL Class A holders
Semi Truck Drivers

Industry/Entity Type

Trucking Company

Font styles to use
Other font styles liked:
• a font to match my logo

Requirements
Must have
• "Make up to $90,000"
"brisklanefreighters.com"
"503-217-6095"

```html
<!DOCTYPE html>
<html lang="en">
<head>
<meta charset="UTF-8">
<title>Brisklane Freighters – Hiring CDL Drivers Billboard</title>
<link rel="stylesheet" href="https://fonts.googleapis.com/css2?family=Exo+2:ital,wght@0,700;0,800;0,900;1,700;1,800;1,900&display=swap">
<style>
  :root {
    --backdrop: #e9edf2;
    --paper: #f4f4f5;
    --paper-shade: #e4e4e6;
    --ink: #151515;
    --brand-green: #14220f;
    --orange: #f07d0a;
    --red: #e30f16;
    --white: #ffffff;
    --band: #161616;
  }
  * { box-sizing: border-box; margin: 0; padding: 0; }
  html, body { width: 1200px; height: 840px; overflow: hidden; }
  body {
    background: var(--backdrop);
    font-family: "Exo 2", "Arial Narrow", sans-serif;
    position: relative;
  }
  .billboard {
    position: absolute;
    left: 0; top: 234px;
    width: 1200px; height: 372px;
    background: linear-gradient(125deg, var(--paper) 0%, var(--paper) 30%, var(--paper-shade) 31%, var(--paper) 36%, var(--paper) 100%);
    overflow: hidden;
  }
  .photo-strip { position: absolute; left: 0; top: 0; width: 1200px; height: 316px; }
  .brand-name {
    position: absolute; left: 48px; top: 26px;
    font-weight: 900; font-size: 34px; line-height: 0.95;
    color: var(--brand-green); letter-spacing: 0.5px;
    text-transform: uppercase;
  }
  .brand-name span { display: block; }
  .earn-band {
    position: absolute; left: 0; top: 112px;
    width: 360px; height: 42px;
  }
  .earn-band svg { position: absolute; inset: 0; }
  .earn-text {
    position: absolute; left: 70px; top: 5px;
    font-style: italic; font-weight: 800; font-size: 32px; line-height: 1;
    letter-spacing: 4px; color: var(--white);
  }
  .salary {
    position: absolute; left: 44px; top: 158px;
    font-style: italic; font-weight: 900; font-size: 72px; line-height: 1;
    color: var(--orange); letter-spacing: 1px;
  }
  .per-year {
    position: absolute; left: 28px; top: 222px;
    font-style: italic; font-weight: 900; font-size: 70px; line-height: 1;
    color: var(--ink); letter-spacing: -1px;
  }
  .hiring-tag {
    position: absolute; left: 298px; top: 234px;
    width: 298px; height: 42px;
  }
  .hiring-tag svg { position: absolute; inset: 0; }
  .hiring-text {
    position: absolute; left: 28px; top: 9px;
    font-weight: 800; font-size: 23px; line-height: 1; color: var(--white);
    letter-spacing: 0.5px;
  }
  .contact-band {
    position: absolute; left: 0; bottom: 0;
    width: 1200px; height: 56px;
    background: var(--band);
    display: flex; align-items: center;
    padding-left: 30px;
    color: var(--white);
    font-style: italic; font-weight: 900; line-height: 1;
  }
  .icon-badge {
    width: 34px; height: 34px; border-radius: 50%;
    background: var(--orange);
    display: flex; align-items: center; justify-content: center;
    flex: none;
  }
  .web-address { margin-left: 16px; font-size: 34px; }
  .web-address .domain { color: var(--orange); }
  .divider { margin: 0 30px 0 50px; font-size: 36px; font-weight: 700; }
  .phone-number { margin-left: 14px; font-size: 46px; letter-spacing: 1px; }
</style>
</head>
<body>
  <section class="billboard">
    <svg class="photo-strip" viewBox="0 0 1200 316">
      <defs>
        <linearGradient id="forestTruck" x1="0" y1="0" x2="0" y2="1">
          <stop offset="0" stop-color="#3f5a3f"/>
          <stop offset="0.55" stop-color="#b52a22"/>
          <stop offset="1" stop-color="#5a4a44"/>
        </linearGradient>
        <linearGradient id="cloudTruck" x1="0" y1="0" x2="0" y2="1">
          <stop offset="0" stop-color="#8d949a"/>
          <stop offset="0.55" stop-color="#a9b8ae"/>
          <stop offset="1" stop-color="#3b3d3f"/>
        </linearGradient>
        <linearGradient id="blueTruck" x1="0" y1="0" x2="0" y2="1">
          <stop offset="0" stop-color="#cfd6de"/>
          <stop offset="0.5" stop-color="#3d8fb0"/>
          <stop offset="1" stop-color="#4a4d52"/>
        </linearGradient>
      </defs>
      <polygon role="img" aria-label="Photo of a red semi truck hauling a load on a wet road by snowy pine trees" points="529,0 765,0 717,316 473,316" fill="url(#forestTruck)"/>
      <polygon role="img" aria-label="Photo of a sage green semi truck under a cloudy sky" points="777,0 1000,0 970,316 729,316" fill="url(#cloudTruck)"/>
      <polygon role="img" aria-label="Photo of a blue semi truck with chrome grille on a wet lot" points="1012,0 1200,0 1200,316 982,316" fill="url(#blueTruck)"/>
    </svg>

    <h1 class="brand-name"><span>Brisklane</span><span>Freighters</span></h1>

    <div class="earn-band">
      <svg viewBox="0 0 360 42" width="360" height="42">
        <polygon points="0,4 360,0 352,40 0,42" fill="var(--orange)"/>
        <polyline points="12,7 26,21 12,35" fill="none" stroke="var(--white)" stroke-width="5"/>
        <polyline points="32,7 46,21 32,35" fill="none" stroke="var(--white)" stroke-width="5"/>
      </svg>
      <span class="earn-text">EARN UP TO</span>
    </div>

    <div class="salary">$90,000</div>
    <div class="per-year">A YEAR</div>

    <div class="hiring-tag">
      <svg viewBox="0 0 298 42" width="298" height="42">
        <polygon points="10,2 298,0 290,40 0,42" fill="var(--red)"/>
      </svg>
      <span class="hiring-text">HIRING CDL DRIVERS</span>
    </div>

    <footer class="contact-band">
      <span class="icon-badge">
        <svg width="22" height="22" viewBox="0 0 22 22" fill="none" stroke="#fff" stroke-width="1.6">
          <circle cx="11" cy="11" r="9"/>
          <ellipse cx="11" cy="11" rx="4" ry="9"/>
          <line x1="2" y1="11" x2="20" y2="11"/>
          <line x1="4" y1="6" x2="18" y2="6"/>
          <line x1="4" y1="16" x2="18" y2="16"/>
        </svg>
      </span>
      <span class="web-address">www.<span class="domain">brisklanefreighters</span>.com</span>
      <span class="divider">/</span>
      <span class="icon-badge">
        <svg width="20" height="20" viewBox="0 0 24 24" fill="#fff">
          <path d="M6.6 10.8a15.1 15.1 0 0 0 6.6 6.6l2.2-2.2a1 1 0 0 1 1-.25 11.4 11.4 0 0 0 3.6.57 1 1 0 0 1 1 1V20a1 1 0 0 1-1 1A17 17 0 0 1 3 4a1 1 0 0 1 1-1h3.5a1 1 0 0 1 1 1c0 1.25.2 2.45.57 3.57a1 1 0 0 1-.25 1z"/>
        </svg>
      </span>
      <span class="phone-number">503-217-6095</span>
    </footer>
  </section>
</body>
</html>
```